Kitchen and custom cabinetry company looking for business card design

We make: * Custom Kitchens, contemporary and traditional kitchens, Vanities, Libraries, Custom Entry Doors, Custom Wine Cellars and Custom Design Furniture. Phone number 555-271-4486. Address: Marlowe Bay NY. Email: TOLVANE@mailbox-example.com Portfolio at: TOLVANEcabinetry.example I would like moderns fonts and not heavy lines. double side but maybe will use clear plastic. I attached the logo.

```html
<!DOCTYPE html>
<html lang="en">
<head>
<meta charset="utf-8">
<title>TOLVANE Cabinetry – Business Card</title>
<link rel="stylesheet" href="https://fonts.googleapis.com/css2?family=Quicksand:wght@500;700&display=swap">
<style>
  :root {
    --backdrop: #7480bc;
    --card-face: #ecedf0;
    --card-highlight: #f8f8fa;
    --accent-orange: #d9603a;
    --band-grey: #7d7e82;
    --band-grey-light: #c4c5c9;
    --ink-dark: #4d4744;
    --logo-grey: #85868a;
  }
  * { box-sizing: border-box; margin: 0; padding: 0; }
  html, body {
    width: 1200px;
    height: 1000px;
    overflow: hidden;
    background: var(--backdrop);
    font-family: "Quicksand", sans-serif;
  }
  .stage {
    position: relative;
    width: 1200px;
    height: 1000px;
  }
  .card {
    position: absolute;
    width: 630px;
    height: 360px;
    border-radius: 10px;
    overflow: hidden;
    background: var(--card-face);
    box-shadow: 0 14px 30px rgba(30, 36, 80, 0.28);
  }
  .card--front { left: 80px; top: 110px; }
  .card--back  { left: 490px; top: 530px; }
  .card__art {
    position: absolute;
    inset: 0;
    width: 100%;
    height: 100%;
  }
  .contact-list {
    position: absolute;
    left: 0;
    top: 132px;
    list-style: none;
  }
  .contact-list__item {
    height: 44px;
    margin-bottom: 16px;
    padding-left: 34px;
    display: flex;
    align-items: center;
    background: var(--accent-orange);
    color: var(--ink-dark);
    font-weight: 700;
    font-size: 21px;
    letter-spacing: 0.3px;
    white-space: nowrap;
  }
  .contact-list__item--address { width: 400px; }
  .contact-list__item--email   { width: 420px; }
  .contact-list__item--web     { width: 380px; }
  .brand {
    position: absolute;
    display: flex;
    align-items: center;
    gap: 10px;
    color: var(--logo-grey);
    font-weight: 700;
    white-space: nowrap;
  }
  .brand__mark {
    background: var(--accent-orange);
    flex: none;
  }
  .brand--small { right: 34px; top: 66px; font-size: 24px; letter-spacing: 2px; }
  .brand--small .brand__mark { width: 13px; height: 13px; }
  .brand--large { left: 0; right: 0; top: 148px; justify-content: center; font-size: 34px; letter-spacing: 3px; }
  .brand--large .brand__mark { width: 19px; height: 19px; }
</style>
</head>
<body>
<main class="stage">

  <section class="card card--front" aria-label="Business card, contact side">
    <svg class="card__art" viewBox="0 0 630 360" preserveAspectRatio="none" aria-hidden="true">
      <path d="M0 0 H430 C320 18 170 40 0 78 Z" fill="var(--accent-orange)"/>
      <path d="M0 78 C170 40 320 18 430 0 H470 C330 30 170 70 0 120 Z" fill="var(--card-highlight)"/>
      <path d="M630 360 H120 C330 340 500 300 630 215 Z" fill="var(--band-grey-light)"/>
      <path d="M630 360 H330 C450 345 560 310 630 265 Z" fill="var(--band-grey)"/>
    </svg>
    <div class="brand brand--small">
      <span class="brand__mark"></span>
      <span class="brand__name">TOLVANE CABINETRY INC.</span>
    </div>
    <ul class="contact-list">
      <li class="contact-list__item contact-list__item--address">A : Marlowe Bay NY</li>
      <li class="contact-list__item contact-list__item--email">E : TOLVANE@mailbox-example.com</li>
      <li class="contact-list__item contact-list__item--web">W : TOLVANEcabinetry.example</li>
    </ul>
  </section>

  <section class="card card--back" aria-label="Business card, brand side">
    <svg class="card__art" viewBox="0 0 630 360" preserveAspectRatio="none" aria-hidden="true">
      <path d="M0 0 H300 C200 12 100 26 0 46 Z" fill="var(--accent-orange)"/>
      <path d="M0 46 C100 26 200 12 300 0 H340 C220 22 110 50 0 84 Z" fill="var(--card-highlight)"/>
      <path d="M630 360 H380 C500 340 580 300 630 250 Z" fill="var(--band-grey-light)"/>
      <path d="M630 360 H500 C560 345 610 320 630 295 Z" fill="var(--band-grey)"/>
    </svg>
    <div class="brand brand--large">
      <span class="brand__mark"></span>
      <span class="brand__name">TOLVANE CABINETRY INC.</span>
    </div>
  </section>

</main>
</body>
</html>
```